Construction material supplies company business card ****

1. Full company name “Marlow Aggregate Products Ltd”
I am after a Business card design for the company as a whole. We are better known in Solomon Islands as “Marlow Aggregate” for short.

We are a building materials supplier of
Ready Mixed Concrete, Bricks and Blocks,
Quarry products- gravel, aggregates, sand etc.
Cement distributor/retailer of reputable brands.
Other prefab concrete products. Culverts, wave breakers, concrete retaining blocks etc.

2. Competitive Advantage over Competition: Quality, efficient, professional, dependable, reliable

3. We want people to feel trust worthy, high quality, strong when they see our brand

5. No preference to color. Maybe more sturdy and corporate. Not fancy.

Industry/Entity Type

CONSTRUCTION SUPPLY

Contact Information for Business Card

Name, Position, office phone mob phone, email

Requirements
Must have
• the company logo
Nice to have
• would like to see a mixture of designs, of with logo only and also with simple graphic designs to bring out the company whilst still have the strong sturdy professional feeling

```html
<!DOCTYPE html>
<html lang="en">
<head>
<meta charset="utf-8">
<title>Marlow Aggregate – Business Card</title>
<link rel="stylesheet" href="https://fonts.googleapis.com/css2?family=Montserrat:wght@500;600;700&family=Arimo:wght@400&display=swap">
<style>
  :root {
    --navy: #123f68;
    --navy-deep: #0f3a61;
    --ink: #2b2b2b;
    --muted: #6b6b6b;
    --paper: #ffffff;
    --stage: #e9ebee;
  }
  * { box-sizing: border-box; margin: 0; padding: 0; }
  html, body { width: 1200px; height: 900px; overflow: hidden; }
  body {
    background: var(--stage);
    font-family: "Arimo", Arial, sans-serif;
    position: relative;
  }
  .card {
    position: absolute;
    width: 640px;
    height: 366px;
    box-shadow: 0 10px 28px rgba(0,0,0,.18);
    overflow: hidden;
  }
  .card-front {
    left: 120px; top: 70px;
    background: var(--navy-deep);
  }
  .front-texture {
    position: absolute; inset: 0;
    background: linear-gradient(135deg, #113c65 0%, #0f3a61 55%, #174a78 100%);
  }
  .front-wordmark {
    position: absolute;
    left: 0; right: 0; top: 158px;
    text-align: center;
    font-family: "Montserrat", sans-serif;
    font-weight: 600;
    font-size: 42px;
    letter-spacing: 3px;
    color: var(--paper);
    text-transform: uppercase;
  }
  .card-back {
    left: 440px; top: 464px;
    background: var(--paper);
  }
  .back-wordmark {
    position: absolute;
    right: 40px; top: 34px;
    font-family: "Montserrat", sans-serif;
    font-weight: 600;
    font-size: 30px;
    letter-spacing: 2px;
    color: var(--navy);
    text-transform: uppercase;
  }
  .edge-tab {
    position: absolute;
    right: 0; top: 120px;
    width: 12px; height: 52px;
    background: var(--navy);
    border-radius: 6px 0 0 6px;
  }
  .person {
    position: absolute;
    right: 40px; top: 122px;
    text-align: right;
  }
  .person-name {
    font-family: "Montserrat", sans-serif;
    font-weight: 700;
    font-size: 22px;
    color: var(--navy);
  }
  .person-role {
    font-family: "Montserrat", sans-serif;
    font-weight: 500;
    font-size: 12px;
    color: var(--muted);
    margin-top: 2px;
  }
  .contact-list {
    position: absolute;
    right: 36px; bottom: 34px;
    list-style: none;
  }
  .contact-item {
    display: flex;
    justify-content: flex-end;
    align-items: center;
    gap: 12px;
    font-size: 15px;
    color: var(--ink);
    line-height: 26px;
  }
  .contact-icon { width: 16px; height: 16px; flex: none; }
  .contact-icon * { fill: var(--navy); }
</style>
</head>
<body>
  <section class="card card-front">
    <div class="front-texture" role="img" aria-label="Subtle repeating brand pattern in deep navy tones"></div>
    <div class="front-wordmark">Marlow Aggregate</div>
  </section>

  <section class="card card-back">
    <div class="back-wordmark">Marlow Aggregate</div>
    <div class="edge-tab"></div>
    <div class="person">
      <div class="person-name">Daniel Rourke</div>
      <div class="person-role">Director</div>
    </div>
    <ul class="contact-list">
      <li class="contact-item">677 24 5510
        <svg class="contact-icon" viewBox="0 0 16 16"><path d="M3.6 1.5l2.3 2.6-1.3 1.8c.9 2 2.5 3.6 4.5 4.5l1.8-1.3 2.6 2.3-1.4 2.2c-5.3-.6-9.4-4.7-10-10z"/></svg>
      </li>
      <li class="contact-item">677 24 5510
        <svg class="contact-icon" viewBox="0 0 16 16"><path d="M4.5 1h7a1 1 0 0 1 1 1v12a1 1 0 0 1-1 1h-7a1 1 0 0 1-1-1V2a1 1 0 0 1 1-1zm.5 2v9h6V3zm3 10a.8.8 0 1 0 0 1.6A.8.8 0 0 0 8 13z"/></svg>
      </li>
      <li class="contact-item">info@marlowaggregate.com
        <svg class="contact-icon" viewBox="0 0 16 16"><path d="M1 3.5h14v9H1zm1.5 1.2v.3L8 9l5.5-4v-.3zm0 2.2v4.4h11V6.9L8 10.8z"/></svg>
      </li>
      <li class="contact-item">www.marlowaggregate.com
        <svg class="contact-icon" viewBox="0 0 16 16"><circle cx="8" cy="8" r="7"/></svg>
      </li>
    </ul>
  </section>
</body>
</html>
```